Lawn mowing business card design

We need a business card design for our lawn mowing and gardening business which is located in the Northern Beaches of Sydney. Our business name is Meadowline Turf and our logo is predominantly green and yellow in color. Please see our website at www.meadowlineturf.com.au for design ideas. The business targets young professionals and older clientele. As such the font should be easy to read, but I also want the business card to be colorful and stand out.

Target Market(s)

young professionals

Industry/Entity Type

Lawn Care

Contact Information for Business Card

Meadowline Turf, Gareth Pellow, 0478559201, www.meadowlineturf.com.au, email: meadowlineturf@mailbox-example.com

Font styles to use
Serif

Colors
9bcb3b
fbed22

Requirements
Must have
• Must include the details listed above. Must include the attached logo.
Nice to have
• Logo attached with two copies. The logo without any writing is high quality, please feel free to be creative with the text stating our business name "Meadowline Turf" using this file.

```html
<!DOCTYPE html>
<html lang="en">
<head>
<meta charset="utf-8">
<title>Meadowline Turf – Business Card</title>
<link rel="stylesheet" href="https://fonts.googleapis.com/css2?family=Montserrat:wght@600;700&family=Carlito&display=swap">
<style>
  :root {
    --canvas-bg: #e6e8e4;
    --card-bg: #f1f1f1;
    --leaf-green: #7dc242;
    --deep-green: #2a8c3f;
    --charcoal: #3c3c3c;
    --body-text: #555555;
    --white: #ffffff;
  }
  * { margin: 0; padding: 0; box-sizing: border-box; }
  html, body { width: 1200px; height: 800px; overflow: hidden; }
  body {
    background: var(--canvas-bg);
    display: flex;
    align-items: center;
    justify-content: center;
    gap: 40px;
  }
  .card {
    position: relative;
    width: 520px;
    height: 298px;
    background: var(--card-bg);
    overflow: hidden;
    box-shadow: 0 6px 18px rgba(0,0,0,0.12);
  }
  .card-shapes { position: absolute; inset: 0; width: 100%; height: 100%; }

  /* Front */
  .brand {
    position: absolute;
    inset: 0;
    display: flex;
    align-items: center;
    justify-content: center;
    gap: 14px;
  }
  .brand-dot {
    width: 22px; height: 22px;
    border-radius: 50%;
    background: var(--deep-green);
  }
  .brand-name {
    font-family: "Montserrat", sans-serif;
    font-weight: 700;
    font-size: 32px;
    color: var(--charcoal);
  }

  /* Back */
  .holder-name {
    position: absolute;
    left: 82px; top: 121px;
    font-family: "Montserrat", sans-serif;
    font-weight: 600;
    font-size: 22px;
    letter-spacing: 0.5px;
    color: var(--white);
    text-transform: uppercase;
  }
  .contact-list {
    position: absolute;
    left: 78px; top: 186px;
    list-style: none;
    font-family: "Carlito", sans-serif;
    font-size: 16px;
    color: var(--body-text);
  }
  .contact-item {
    display: flex;
    align-items: center;
    gap: 8px;
    height: 27px;
  }
  .contact-icon { width: 14px; height: 14px; flex: none; }
</style>
</head>
<body>

  <section class="card card-front">
    <svg class="card-shapes" viewBox="0 0 520 298" aria-hidden="true">
      <polygon points="0,150 22,168 22,298 0,298" fill="var(--leaf-green)"/>
      <polygon points="498,0 520,0 520,150 498,128" fill="var(--deep-green)"/>
    </svg>
    <div class="brand">
      <span class="brand-dot"></span>
      <span class="brand-name">Meadowline Turf</span>
    </div>
  </section>

  <section class="card card-back">
    <svg class="card-shapes" viewBox="0 0 520 298" aria-hidden="true">
      <polygon points="0,88 72,88 58,166 0,166" fill="var(--leaf-green)"/>
      <polygon points="72,88 96,100 70,100" fill="var(--deep-green)"/>
      <polygon points="60,106 410,106 410,166 48,166" fill="var(--charcoal)"/>
      <path d="M402 0 C388 90 408 190 352 298" fill="none" stroke="var(--leaf-green)" stroke-width="4"/>
      <path d="M424 0 C408 90 428 190 372 298 L520 298 L520 0 Z" fill="var(--leaf-green)"/>
    </svg>

    <h1 class="holder-name">Gareth Pellow</h1>

    <ul class="contact-list">
      <li class="contact-item">
        <svg class="contact-icon" viewBox="0 0 16 16" aria-hidden="true">
          <circle cx="8" cy="8" r="7" fill="none" stroke="var(--deep-green)" stroke-width="1.5"/>
          <path d="M5.5 4.5 L7 6 L6.2 7 C6.8 8.3 7.7 9.2 9 9.8 L10 9 L11.5 10.5 L10.5 11.6 C7.5 11 5 8.5 4.4 5.5 Z" fill="var(--deep-green)"/>
        </svg>
        <span>0478559201</span>
      </li>
      <li class="contact-item">
        <svg class="contact-icon" viewBox="0 0 16 16" aria-hidden="true">
          <g fill="none" stroke="var(--deep-green)" stroke-width="1.3">
            <circle cx="8" cy="8" r="6.5"/>
            <ellipse cx="8" cy="8" rx="3" ry="6.5"/>
            <line x1="1.5" y1="8" x2="14.5" y2="8"/>
            <line x1="2.5" y1="4.5" x2="13.5" y2="4.5"/>
            <line x1="2.5" y1="11.5" x2="13.5" y2="11.5"/>
          </g>
        </svg>
        <span>www.meadowlineturf.com.au</span>
      </li>
      <li class="contact-item">
        <svg class="contact-icon" viewBox="0 0 16 16" aria-hidden="true">
          <rect x="1.5" y="3.5" width="13" height="9" fill="var(--deep-green)"/>
          <path d="M1.5 3.5 L8 9 L14.5 3.5" fill="none" stroke="var(--card-bg)" stroke-width="1.2"/>
        </svg>
        <span>meadowlineturf@mailbox-example.com</span>
      </li>
    </ul>
  </section>

</body>
</html>
```